Signage for a store*

logo on the two sides of the sign
in the middle is the name of the store witch is KORVELO
at the bottom of the two logos, one side for location/address and the other side is contact details phone number is 718-392-6170 address is 7342 THE SIGN WILL BEE 15 FEET BY 4 FEET I WOULD LIKE THAT THE
BACKGROUND OF THE SIGN SHOULD HAVE A NICE COLOR BASE
THAT GOES FOR A WINE STORE

```html
<!DOCTYPE html>
<html lang="en">
<head>
<meta charset="utf-8">
<title>KORVELO Wine Store Sign</title>
<link rel="stylesheet" href="https://fonts.googleapis.com/css2?family=Josefin+Sans:wght@400&family=Arimo:wght@700&family=Josefin+Slab:wght@400&display=swap">
<style>
  :root {
    --wine: #a4384f;
    --gold: #b5893f;
    --ink: #333333;
    --paper: #ffffff;
    --sign-type: #ffffff;
  }
  html, body {
    margin: 0;
    padding: 0;
    width: 1200px;
    height: 1200px;
    overflow: hidden;
    background: var(--paper);
  }
  .sheet {
    display: block;
    width: 1200px;
    height: 1200px;
  }
  .dimension-line { stroke: var(--ink); stroke-width: 1; fill: none; }
  .dimension-label {
    font-family: "Arimo", Arial, sans-serif;
    font-weight: 700;
    font-size: 32px;
    fill: var(--ink);
  }
  .sign-panel { fill: var(--wine); }
  .sign-frame { fill: none; stroke: var(--gold); stroke-width: 2.5; }
  .sign-text {
    font-family: "Josefin Sans", "Futura", sans-serif;
    font-weight: 400;
    fill: var(--sign-type);
  }
  .sign-heading { font-size: 98px; }
  .sign-number { font-size: 112px; }
  .sign-phone-label { font-size: 30px; }
  .sign-phone { font-size: 37px; }
  .brand-name {
    font-family: "Josefin Sans", "Futura", sans-serif;
    font-weight: 400;
  }
  .brand-name--sign { fill: var(--gold); font-size: 46px; }
  .brand-name--display { fill: var(--wine); font-size: 72px; }
  .brand-dot--sign { fill: none; stroke: var(--gold); stroke-width: 2.5; }
  .brand-dot--display { fill: none; stroke: var(--wine); stroke-width: 3; }
</style>
</head>
<body>
<svg class="sheet" viewBox="0 0 1200 1200" xmlns="http://www.w3.org/2000/svg">
  <!-- width dimension -->
  <g class="dimension dimension--width">
    <text class="dimension-label" x="374" y="78" text-anchor="middle">4 feet</text>
    <line class="dimension-line" x1="221" y1="91" x2="499" y2="91"/>
    <line class="dimension-line" x1="221" y1="79" x2="221" y2="103"/>
    <line class="dimension-line" x1="499" y1="79" x2="499" y2="103"/>
  </g>

  <!-- height dimension -->
  <g class="dimension dimension--height">
    <line class="dimension-line" x1="528" y1="114" x2="528" y2="1156"/>
    <line class="dimension-line" x1="514" y1="114" x2="539" y2="114"/>
    <line class="dimension-line" x1="514" y1="1156" x2="539" y2="1156"/>
    <text class="dimension-label" x="603" y="672" text-anchor="middle">15 feet</text>
  </g>

  <!-- sign face -->
  <g class="sign">
    <rect class="sign-panel" x="222" y="114" width="278" height="1042"/>
    <path class="sign-frame" d="M244,124 H478 A13,13 0 0 0 491,137 V1134 A13,13 0 0 0 478,1147 H244 A13,13 0 0 0 231,1134 V137 A13,13 0 0 0 244,124 Z"/>

    <text class="sign-text sign-heading" x="361" y="256" text-anchor="middle" textLength="226" lengthAdjust="spacingAndGlyphs">WINE</text>
    <text class="sign-text sign-heading" x="361" y="328" text-anchor="middle" textLength="226" lengthAdjust="spacingAndGlyphs">STORE</text>

    <text class="sign-text sign-number" x="361" y="592" text-anchor="middle" textLength="222" lengthAdjust="spacingAndGlyphs">7342</text>

    <text class="sign-text sign-phone-label" x="361" y="735" text-anchor="middle">phone</text>
    <text class="sign-text sign-phone" x="361" y="778" text-anchor="middle" textLength="232" lengthAdjust="spacingAndGlyphs">718-392-6170</text>

    <g class="brand brand--sign">
      <circle class="brand-dot--sign" cx="361" cy="930" r="14"/>
      <text class="brand-name brand-name--sign" x="361" y="1010" text-anchor="middle" textLength="196" lengthAdjust="spacingAndGlyphs">KORVELO</text>
    </g>
  </g>

  <!-- brand name display -->
  <g class="brand brand--display">
    <circle class="brand-dot--display" cx="913" cy="540" r="20"/>
    <text class="brand-name brand-name--display" x="913" y="650" text-anchor="middle" textLength="326" lengthAdjust="spacingAndGlyphs">KORVELO</text>
  </g>
</svg>
</body>
</html>
```